4 panel (or page) brochure

We need a brochure design for a Oklahoma based company. We manufacture and sell underground and below ground shelters. We sell our shelters in our local showroom, as well distribute our shelters to a big box national retailer. I would like to have a simple design that includes a few pictures of our product and details on each product we offer as well as install details for each product. Our out of state retailers likely will not have our product display so we will need something that sells the product without seeing it in person.

I would like something that it easily printable as well as able to edit at a later time if needed.

I've included Catalog/Brochure Copy
Pictures of Below Ground Units/Above Ground Units - feel free to edit or touch up.
Some brochure ideas I found on LayoutNest that seemed to be similar to what we can do.
The Inside of a brochure we did a while back that we liked (style-wise)
A general info flyer for more information

It Company

```html
<!DOCTYPE html>
<html lang="en">
<head>
<meta charset="utf-8">
<title>StormHaven Shelters Brochure</title>
<link href="https://fonts.googleapis.com/css2?family=Open+Sans:ital,wght@0,400;0,600;0,700;1,400&family=Kaushan+Script&display=swap" rel="stylesheet">
<style>
:root{
  --backdrop:#4a4a4a;
  --red:#b3202c;
  --red-dark:#8f1820;
  --red-light:#c93a44;
  --ink:#1a1a1a;
  --rule:#c1272d;
  --gray-panel:#e9e9e9;
  --white:#ffffff;
}
*{margin:0;padding:0;box-sizing:border-box}
html,body{width:1200px;height:874px;overflow:hidden;background:var(--backdrop);font-family:"Open Sans",Arial,sans-serif;color:var(--ink)}
.spread{position:absolute;left:26px;top:49px;width:1160px;height:750px;display:flex;box-shadow:0 2px 8px rgba(0,0,0,.4)}
.page-left{position:relative;width:580px;height:750px}
.page-right{position:relative;width:580px;height:750px;background:linear-gradient(100deg,#fdfdfd 0%,#e6e6e6 40%,#d4d4d4 100%);overflow:hidden}
.band-red{position:absolute;left:0;width:580px;background:linear-gradient(100deg,var(--red-dark) 0%,var(--red) 45%,var(--red-light) 75%,var(--red) 100%);color:var(--white)}
.benefits{top:0;height:172px;padding:20px 16px 0 31px;border-bottom:3px solid #111}
.contact{top:584px;height:166px;padding:32px 0 0 24px;border-top:4px solid #111}
.middle{position:absolute;left:0;top:175px;width:580px;height:409px;background:linear-gradient(100deg,#f4f4f4 0%,#dcdcdc 45%,#fafafa 70%,#e2e2e2 100%)}
h2{font-size:15px;font-weight:700;text-transform:uppercase;letter-spacing:.1px;position:relative;padding-bottom:7px;margin-bottom:9px}
h2::after{content:"";position:absolute;left:0;bottom:0;width:290px;height:2px;background:var(--white)}
.middle h2::after,.page-right h2::after{background:var(--rule);width:280px;height:1px}
.page-right h2::after{width:255px}
.benefits p{font-size:10.3px;line-height:13px;margin-bottom:6px}
.options{position:absolute;left:29px;top:27px;width:300px}
.options h3{font-size:11px;font-weight:700;margin-bottom:4px}
.options p,.install p{font-size:10px;line-height:19.5px}
.options .group{margin-bottom:17px}
.options h2,.install h2{font-size:14.5px}
.install{position:absolute;left:29px;top:299px;width:420px}
.install h2{margin-bottom:9px}
.install p{line-height:19.5px}
.door-photo{position:absolute;left:338px;top:20px;width:227px;height:282px;border:3px solid #111;background:linear-gradient(160deg,#8a8a8a 0%,#d9d9d9 35%,#eeeeee 60%,#9d9d9d 100%)}
.contact h2{font-size:15px;margin-bottom:14px}
.contact h2::after{display:none}
.contact p{font-size:10.6px;line-height:21px}
.brand{position:absolute;left:396px;top:72px;display:flex;align-items:center;gap:8px;color:var(--white);font-size:20px;font-weight:700}
.brand-dot{width:16px;height:16px;border-radius:50%;background:var(--white)}
.testimonials{position:absolute;left:24px;top:17px;width:530px}
.testimonials h2{margin-bottom:21px}
.quote{font-size:9.6px;font-style:italic;line-height:19.5px;margin-bottom:13px}
.author{font-size:11px;font-weight:700;margin-bottom:30px}
.tagline{position:absolute;left:34px;top:341px;font-family:"Kaushan Script",cursive;font-size:34px;color:#000;letter-spacing:.5px}
.family-photo{position:absolute;left:12px;top:392px;width:545px;height:358px;background:radial-gradient(ellipse at 55% 55%,#c9a58a 0%,#e0d2c6 40%,#e8e8e8 70%,#d9d9d9 100%)}
</style>
</head>
<body>
<div class="spread">
  <section class="page-left">
    <div class="band-red benefits">
      <h2>Above Ground Shelter Benefits:</h2>
      <p>Our above ground units have a 36” side door, flat to the ground, which means they are wide enough and flat enough to be wheel chair accessible.</p>
      <p>Our above ground units are typically installed in about 2 hours.</p>
      <p>A variety of sizes to suit your need</p>
      <p>All units come standard with a bulletproof lookout glass</p>
      <p>Can also be used as a panic room</p>
    </div>
    <div class="middle">
      <div class="options">
        <h2>Above Ground Shelter Options:</h2>
        <div class="group">
          <h3>Door location:</h3>
          <p>End Door (Short Side)<br>Side Door (Long Side Right)<br>Side Door (Long Side Left)</p>
        </div>
        <div class="group">
          <h3>Door opening:</h3>
          <p>Choice of door opening to the outside or inside of shelter</p>
        </div>
        <div class="group">
          <h3>Door hinges:</h3>
          <p>Hinges can be placed on right side or left side of door.</p>
        </div>
      </div>
      <div class="door-photo" role="img" aria-label="Photo of an open white steel shelter door with a lookout window"></div>
      <div class="install">
        <h2>Installation Process:</h2>
        <p>Shelter is placed with an excavator and bolted to concrete with 4 ¾ inch bolts<br>Can be installed outside on a concrete slab of at least 15”-20”</p>
      </div>
    </div>
    <div class="band-red contact">
      <h2>Call or visit our showroom today!</h2>
      <p>4120 S. PRAIRIE RD OKLAHOMA CITY, OK 73100<br>OFFICE 405-555-0147<br>INFO@STORMHAVEN.EXAMPLE</p>
      <div class="brand"><span class="brand-dot"></span><span>STORMHAVEN</span></div>
    </div>
  </section>
  <section class="page-right">
    <div class="testimonials">
      <h2>What Our Clients Say</h2>
      <p class="quote">StormHaven Certified Storm Shelters installed a walk-in storm shelter at my parents' home recently, and i just can't begin to say how professional they were and what a great job they did! My parents are not physically able to climb down into an underground shelter any longer, so we began researching our options for walk-in shelter to have installed at their home. Hopefully they won't ever have to use it, but it is certainly peace of mind for them and for my brother and I. Thank you STORMHAVEN!!</p>
      <p class="author">-Marla Dean Whitley</p>
      <p class="quote">My good friend Curtis Hollande and his company StormHaven installed my family's shelter today! Top Notch job!! Definitely recommend them!!</p>
      <p class="author">-Glen Parker</p>
    </div>
    <p class="tagline">Protect your family today</p>
    <div class="family-photo" role="img" aria-label="Photo of a smiling family of four, parents with a daughter and son"></div>
  </section>
</div>
</body>
</html>
```